Landing Page and Logo for Auto-Blogging Platform

I created a platform that allows users to start a blog for their business, hobby, charity, etc. I need a landing page where users can learn about the platform, benefits of consistent blogging, SEO value, plans/pricing, etc. The landing page needs to have multiple call to action buttons encouraging the visitor to register/sign up for a free trial.

In addition to the landing page, I need a page for users to establish the settings for their blog. This page should be a fairly simple form, intended for the user to enter a few details to set up their blog:
1. Name of Blog
2. Up to 10 topics and/or keywords the blog should focus on
3. Theme: Color-scheme and logo upload for blog.

I have attached the specifications of the platform's functionality so you can better understand how it works, plans/pricing, etc.

I also need a logo for the business. The name of the platform is PostNook.

Target Market(s)

Website owners, bloggers, business owners

Industry/Entity Type

Technology, Internet, web design

Coding

Coded - Design and coding required

Number of Pages Required

2 page

Colors
0054AA
0677BA
7BADD7
CADEEF
E8F1F8
0094D4
00A9DD
6FCCEA
C7EBF8
E9F6FB

Requirements
Must have
• Eye-catching design but fairly light on content (keep it simple and brief.)
Nice to have
• Eye-catching yet simple design, clean and easy to understand what we are offering.
Should not have
• Too much “wordy” and confusing content.

```html
<!DOCTYPE html>
<html lang="en">
<head>
<meta charset="utf-8">
<title>PostNook – Automate Your Blog Posting with AI</title>
<link rel="stylesheet" href="https://fonts.googleapis.com/css2?family=Poppins:wght@400;500;600;700&display=swap">
<style>
:root{
  --navy:#07111d;
  --navy-2:#0b1e33;
  --blue-deep:#0054AA;
  --blue:#0677BA;
  --blue-bright:#0094D4;
  --cyan:#00A9DD;
  --sky:#6FCCEA;
  --sky-soft:#C7EBF8;
  --ice:#E9F6FB;
  --ice-2:#E8F1F8;
  --ink:#111827;
  --muted:#6b7280;
  --line:#e5e7eb;
  --peach:#fdf1ec;
}
*{box-sizing:border-box;margin:0;padding:0}
html,body{width:1200px;height:4388px;overflow:hidden}
body{font-family:"Poppins",sans-serif;color:var(--ink);background:#fff;position:relative}
.abs{position:absolute}
.center{text-align:center}
.badge{display:inline-block;font-size:10px;letter-spacing:1.5px;text-transform:uppercase;padding:5px 14px;border-radius:20px;font-weight:500}
.badge-dark{background:rgba(255,255,255,.08);color:#cfe6f5;border:1px solid rgba(255,255,255,.15)}
.badge-light{background:var(--ice);color:var(--blue)}
.btn{display:inline-block;font-size:13px;font-weight:500;padding:11px 22px;border-radius:6px;text-decoration:none}
.btn-primary{background:var(--blue-bright);color:#fff}
.btn-outline{border:1px solid rgba(255,255,255,.6);color:#fff}
.h2{font-size:32px;font-weight:700;text-align:center}

/* Hero */
.hero{top:0;left:0;width:1200px;height:912px;background:radial-gradient(ellipse 700px 420px at 600px 300px,#0d3b5e 0%,#08203a 45%,var(--navy) 100%);color:#fff}
.nav{top:34px;left:140px;width:920px;height:40px;display:flex;align-items:center;justify-content:space-between}
.brand{font-size:22px;font-weight:700;color:#fff;display:flex;align-items:center;gap:8px}
.brand-dot{width:10px;height:10px;border-radius:50%;background:var(--cyan)}
.nav-links{display:flex;gap:28px;font-size:12px;color:#dfe8f0}
.nav-actions{display:flex;gap:10px}
.nav-actions a{font-size:12px;padding:7px 16px;border-radius:5px;color:#fff;text-decoration:none}
.nav-signin{border:1px solid rgba(255,255,255,.6)}
.nav-login{background:var(--blue-bright)}
.hero-badge{top:112px;left:0;width:1200px}
.hero-title{top:150px;left:0;width:1200px;font-size:56px;line-height:66px;font-weight:700}
.hero-title span{color:var(--cyan)}
.hero-text{top:290px;left:330px;width:540px;font-size:13px;line-height:20px;color:#c9d6e2}
.hero-ctas{top:352px;left:0;width:1200px;display:flex;justify-content:center;gap:14px}
.hero-visual{top:420px;left:300px;width:600px;height:330px;border-radius:18px;background:linear-gradient(135deg,#d7dde4 0%,#f3f5f7 50%,#aeb8c3 100%)}
.hero-arrow{top:612px;width:20px;height:20px;color:#7f93a6}

/* Trusted */
.trusted{top:920px;left:190px;width:820px;height:130px;background:var(--peach)}
.trusted h3{position:absolute;top:26px;width:100%;text-align:center;font-size:24px;font-weight:600}
.logo-row{position:absolute;top:82px;left:40px;right:40px;display:flex;justify-content:space-between;align-items:center}
.logo-shape{width:90px;height:22px;background:#c9c9cc;border-radius:4px}
.logo-shape.round{width:30px;height:30px;border-radius:50%}

/* Why choose */
.why-badge{top:1120px;left:0;width:1200px}
.why-title{top:1150px;left:0;width:1200px}
.features{top:1230px;left:190px;width:820px;display:flex;justify-content:space-between}
.feature{width:240px;text-align:center}
.ring{width:64px;height:64px;margin:0 auto 12px}
.feature h4{font-size:16px;font-weight:600;margin-bottom:6px}
.feature p{font-size:11px;line-height:17px;color:var(--muted)}

/* Matters */
.matters{top:1470px;left:0;width:1200px;height:570px;background:radial-gradient(ellipse 600px 300px at 600px 120px,#0b3352 0%,var(--navy) 100%);color:#fff}
.matters-badge{top:1500px;left:0;width:1200px}
.matters-title{top:1530px;left:0;width:1200px;color:#fff}
.benefits{top:1600px;left:190px;width:820px;display:flex;justify-content:space-between;color:#fff}
.benefit{width:250px;display:flex;gap:10px}
.benefit-icon{flex:none;width:30px;height:30px;border-radius:50%;background:var(--blue-bright)}
.benefit h4{font-size:14px;font-weight:600;margin-bottom:4px}
.benefit p{font-size:10px;line-height:15px;color:#b9c7d4}

/* Dashboard */
.dashboard{top:1840px;left:180px;width:840px;height:350px;background:#fff;border-radius:12px;box-shadow:0 20px 50px rgba(0,0,0,.25);overflow:hidden;font-size:10px}
.dash-bar{height:40px;border-bottom:1px solid var(--line);display:flex;align-items:center;padding:0 18px;gap:30px}
.dash-brand{font-weight:700;font-size:16px}
.dash-search{width:220px;height:22px;border-radius:11px;background:#f1f3f5}
.dash-user{margin-left:auto;display:flex;align-items:center;gap:6px}
.dash-user b{color:var(--blue)}
.avatar{width:18px;height:18px;border-radius:50%;background:var(--sky)}
.dash-side{position:absolute;top:40px;left:0;width:110px;bottom:0;border-right:1px solid var(--line);padding:14px;line-height:22px;color:var(--muted)}
.dash-side .active{color:var(--blue)}
.dash-main{position:absolute;top:52px;left:124px;width:560px;bottom:0}
.dash-feed{position:absolute;top:52px;left:700px;width:128px;line-height:20px;color:var(--muted)}
.dash-feed b{color:var(--ink);display:block}
.tile{position:absolute;border-radius:8px;background:linear-gradient(135deg,#7a8fa3,#c9d4de)}
.tile-text{position:absolute;font-size:12px;font-weight:600;line-height:15px}

/* Steps */
.steps-title{top:2258px;left:0;width:1200px}
.steps{top:2320px;left:160px;width:880px;height:180px}
.step{position:absolute;width:150px;height:150px;border-radius:50%;background:#fff;border:6px solid var(--ice-2);box-shadow:0 6px 20px rgba(0,84,170,.08);text-align:center;padding:48px 18px 0;font-size:10px;line-height:14px;font-weight:500}
.step-num{position:absolute;top:-12px;right:4px;width:40px;height:40px;border-radius:50%;background:var(--blue);color:#fff;font-weight:700;font-size:15px;line-height:40px;text-align:center}

/* Plans */
.plans-badge{top:2534px;left:0;width:1200px}
.plans-title{top:2566px;left:0;width:1200px}
.plan{position:absolute;text-align:center}
.plan-basic{top:2636px;left:190px;width:250px;height:430px;background:linear-gradient(180deg,var(--blue-bright),var(--blue-deep));color:#fff;border-radius:8px;box-shadow:0 16px 30px rgba(0,84,170,.3)}
.plan-other{top:2672px;width:250px;height:360px}
.plan-name{font-size:14px;font-weight:500;margin-top:40px}
.plan-price{font-size:30px;font-weight:700;margin-top:4px}
.plan-price small{font-size:13px;font-weight:400}
.plan-rows{margin-top:24px}
.plan-row{height:40px;line-height:40px;font-size:11px}
.plan-other .plan-row:nth-child(odd){background:#f1f2f4}
.plan-basic .plan-row{border-top:1px solid rgba(255,255,255,.25)}
.plan-btn{display:inline-block;margin-top:26px;font-size:11px;padding:10px 24px;border-radius:5px}
.plan-basic .plan-btn{background:#fff;color:var(--blue)}
.plan-other .plan-btn{background:var(--blue);color:#fff}
.plan-icon{width:36px;height:36px;border-radius:8px;margin:0 auto;background:var(--ice)}

/* Testimonials */
.reviews-title{top:3120px;left:0;width:1200px}
.review{position:absolute;top:3196px;width:250px;height:340px;background:#fff;border-radius:8px;box-shadow:0 8px 24px rgba(0,0,0,.08);padding:26px 22px}
.review.faded{opacity:.35}
.review-head{display:flex;gap:10px;align-items:center;margin-bottom:14px}
.review-avatar{width:42px;height:42px;border-radius:50%;background:linear-gradient(135deg,#c7a88e,#8a6d57)}
.review-name{font-size:13px;font-weight:600}
.stars{color:#f5a623;font-size:11px}
.stars span{color:var(--muted);margin-left:4px}
.review p{font-size:11px;line-height:18px;color:#374151}
.dots{top:3576px;left:0;width:1200px;display:flex;justify-content:center;gap:6px}
.dots i{width:6px;height:6px;border-radius:50%;background:#c7d2dc}
.dots i.on{width:14px;border-radius:3px;background:var(--blue)}

/* CTA */
.cta-blob{top:3670px;left:380px;width:820px;height:470px}
.cta-person{top:3690px;left:150px;width:270px;height:440px;border-radius:130px 130px 20px 20px;background:linear-gradient(180deg,#f0c4b8 0%,#e06d7a 45%,#9fb3c4 100%)}
.cta-content{top:3808px;left:560px;width:420px;color:#fff}
.cta-content h2{font-size:30px;line-height:38px;font-weight:700;margin:14px 0 12px}
.cta-content p{font-size:12px;line-height:18px;color:#e0f1fb;margin-bottom:20px}
.cta-content .btn{background:#fff;color:var(--blue)}
.cta-ring{top:3682px;left:1060px;width:24px;height:24px;border-radius:50%;border:4px solid var(--blue-bright);background:#fff}

/* Footer */
.footer{top:4140px;left:0;width:1200px;height:248px;background:var(--navy);color:#fff}
.footer-row{position:absolute;top:96px;left:140px;width:920px;display:flex;justify-content:space-between;align-items:center}
.footer-links{display:flex;gap:26px;font-size:12px;color:#cdd7e0}
.footer-line{position:absolute;top:170px;left:140px;width:920px;height:1px;background:rgba(255,255,255,.15)}
.footer-copy{position:absolute;top:196px;width:100%;text-align:center;font-size:10px;color:#8a99a8}
</style>
</head>
<body>

<!-- Hero -->
<section class="abs hero">
  <header class="abs nav" style="position:absolute">
    <div class="brand"><span class="brand-dot"></span>PostNook</div>
    <nav class="nav-links"><span>Home</span><span>Features</span><span>Pricing</span><span>How it Works</span><span>Blog</span><span>Resources</span></nav>
    <div class="nav-actions"><a class="nav-signin" href="#">Sign In</a><a class="nav-login" href="#">Login</a></div>
  </header>
  <div class="abs hero-badge center"><span class="badge badge-dark">Welcome to PostNook</span></div>
  <h1 class="abs hero-title center">Automate Your Blog<br><span>Posting with AI</span></h1>
  <p class="abs hero-text center">Boost your SEO effortlessly by consistently publishing fresh, keyword-targeted content. Let PostNook run your blog, so you can focus on growing your business.</p>
  <div class="abs hero-ctas"><a class="btn btn-primary" href="#">Start Your 15 days Free Trial</a><a class="btn btn-outline" href="#">Learn more</a></div>
  <div class="abs hero-visual" role="img" aria-label="Two tablets showing PostNook blog dashboards"></div>
  <svg class="abs hero-arrow" style="left:148px" viewBox="0 0 20 20"><path d="M13 4 7 10l6 6" fill="none" stroke="currentColor" stroke-width="2"/></svg>
  <svg class="abs hero-arrow" style="left:1032px" viewBox="0 0 20 20"><path d="M7 4l6 6-6 6" fill="none" stroke="currentColor" stroke-width="2"/></svg>
</section>

<!-- Trusted -->
<section class="abs trusted">
  <h3>Trusted by More Than 100 Brands</h3>
  <div class="logo-row">
    <div class="logo-shape"></div><div class="logo-shape" style="width:70px"></div><div class="logo-shape" style="width:50px"></div><div class="logo-shape round"></div><div class="logo-shape" style="width:70px"></div><div class="logo-shape round"></div>
  </div>
</section>

<!-- Why choose -->
<div class="abs why-badge center"><span class="badge badge-light">Why Us</span></div>
<h2 class="abs why-title h2">Why Choose PostNook?</h2>
<section class="abs features">
  <div class="feature">
    <svg class="ring" viewBox="0 0 64 64"><circle cx="32" cy="32" r="28" fill="none" stroke="#E8F1F8" stroke-width="5"/><circle cx="32" cy="32" r="28" fill="none" stroke="#0094D4" stroke-width="5" stroke-dasharray="130 176" transform="rotate(-90 32 32)"/><path d="M22 33l7 7 13-14" fill="none" stroke="#0677BA" stroke-width="3"/></svg>
    <h4>Simplicity</h4><p>No coding required. Our platform makes it easy for anyone to start and manage a blog.</p>
  </div>
  <div class="feature">
    <svg class="ring" viewBox="0 0 64 64"><circle cx="32" cy="32" r="28" fill="none" stroke="#E8F1F8" stroke-width="5"/><circle cx="32" cy="32" r="28" fill="none" stroke="#0094D4" stroke-width="5" stroke-dasharray="130 176" transform="rotate(-90 32 32)"/><circle cx="32" cy="32" r="8" fill="none" stroke="#0677BA" stroke-width="3"/></svg>
    <h4>Customization</h4><p>Personalize your blog with your brand's colors, logo, and more.</p>
  </div>
  <div class="feature">
    <svg class="ring" viewBox="0 0 64 64"><circle cx="32" cy="32" r="28" fill="none" stroke="#E8F1F8" stroke-width="5"/><circle cx="32" cy="32" r="28" fill="none" stroke="#0094D4" stroke-width="5" stroke-dasharray="130 176" transform="rotate(-90 32 32)"/><path d="M22 40l7-8 6 5 9-12" fill="none" stroke="#0677BA" stroke-width="3"/></svg>
    <h4>SEO Optimized</h4><p>Improve your online visibility with our built-in SEO tools.</p>
  </div>
</section>

<!-- Why consistent blogging matters -->
<section class="abs matters"></section>
<div class="abs matters-badge center"><span class="badge badge-dark">Benefits of Blogging</span></div>
<h2 class="abs matters-title h2">Why Consistent Blogging Matters</h2>
<section class="abs benefits">
  <div class="benefit"><span class="benefit-icon"></span><div><h4>Boost Your SEO</h4><p>Increase your search engine rankings with regularly updated, rich content.</p></div></div>
  <div class="benefit"><span class="benefit-icon"></span><div><h4>Build Authority</h4><p>Establish your brand as a leader in your industry.</p></div></div>
  <div class="benefit"><span class="benefit-icon"></span><div><h4>Engage Your Audience</h4><p>Connect with your audience through valuable and relevant content.</p></div></div>
</section>

<div class="abs dashboard">
  <div class="dash-bar"><span class="dash-brand">PostNook</span><span class="dash-search"></span><span class="dash-user"><span class="avatar"></span>Welcome <b>Mira</b></span></div>
  <div class="dash-side"><b style="color:#111">Menu</b><br><span class="active">Home</span><br>Library<br>Discover<br><b style="color:#111">Playlist</b><br>Good Hits<br>Best of Weekly<br>Global Hits</div>
  <div class="dash-main">
    <div class="tile-text" style="top:10px;left:0;width:110px">Short Sentences Give You the Liberty</div>
    <div class="tile" style="top:10px;left:130px;width:150px;height:110px" role="img" aria-label="Blog post cover photo"></div>
    <div class="tile-text" style="top:130px;left:130px;width:150px;font-size:10px">How to Build a Side Income One Day at a Time</div>
    <div class="tile" style="top:10px;left:300px;width:110px;height:80px" role="img" aria-label="Blog post cover photo"></div>
    <div class="tile-text" style="top:100px;left:300px;width:110px;font-size:10px">6 Powerful Mental Models</div>
    <div class="tile" style="top:10px;left:430px;width:120px;height:80px" role="img" aria-label="Blog post cover photo"></div>
    <div class="tile-text" style="top:100px;left:430px;width:120px;font-size:10px">Why Solitude Is Good</div>
    <div class="tile-text" style="top:170px;left:0;width:110px">3 Ways to Improve your Life</div>
    <div class="tile" style="top:180px;left:130px;width:420px;height:110px" role="img" aria-label="Blog post cover photos"></div>
  </div>
  <div class="dash-feed"><b>Favorite</b>Quick Writing Tips<br>Editing in Ten Minutes<br>Weekly Idea Lists<br>Art Recall<br><b>Top Articles</b>Daily Focus Notes<br>Plan Your Week</div>
</div>

<!-- Steps -->
<h2 class="abs steps-title h2">4 Simple Steps to Set Up Your Auto-Blog</h2>
<section class="abs steps">
  <svg class="abs" style="top:40px;left:0" width="880" height="100" viewBox="0 0 880 100"><path d="M150 50 Q205 0 250 50 M400 50 Q455 100 500 50 M650 50 Q705 0 750 50" fill="none" stroke="#0677BA" stroke-width="2" stroke-dasharray="4 4"/></svg>
  <div class="step" style="left:0;top:0"><span class="step-num">01</span>Select Frequency of Automated Blog Posts<br><span style="color:#6b7280;font-weight:400">Choose daily, weekly or monthly posts</span></div>
  <div class="step" style="left:243px;top:0"><span class="step-num">02</span>Watch Your Blog<br><span style="color:#6b7280;font-weight:400">New posts appear on your blog</span></div>
  <div class="step" style="left:486px;top:0"><span class="step-num">03</span>Edit Your Blog Topics<br><span style="color:#6b7280;font-weight:400">Adjust topics any time</span></div>
  <div class="step" style="left:730px;top:0"><span class="step-num">04</span>Sit Back and Do Something Else<br><span style="color:#6b7280;font-weight:400">We handle the writing</span></div>
</section>

<!-- Plans -->
<div class="abs plans-badge center"><span class="badge badge-light">Plans &amp; Pricing</span></div>
<h2 class="abs plans-title h2">Flexible Plans for Every Need</h2>
<div class="plan plan-basic">
  <div class="plan-name">Basic Plan</div>
  <div class="plan-price">$9.99<small>/mo</small></div>
  <div class="plan-rows"><div class="plan-row">1 blog post</div><div class="plan-row">up to 1,000 words</div><div class="plan-row">Daily or Monthly</div></div>
  <a class="plan-btn" href="#">Choose Plan</a>
</div>
<div class="plan plan-other" style="left:470px">
  <div class="plan-name" style="margin-top:10px">Premium Plan</div>
  <div class="plan-price">$14.99<small>/mo</small></div>
  <div class="plan-rows"><div class="plan-row">1 blog post</div><div class="plan-row">up to 2,000 words</div><div class="plan-row">Daily or Monthly</div></div>
  <a class="plan-btn" href="#">Choose Plan</a>
</div>
<div class="plan plan-other" style="left:760px">
  <div class="plan-name" style="margin-top:10px">Ultimate Plan</div>
  <div class="plan-price">$24.99<small>/mo</small></div>
  <div class="plan-rows"><div class="plan-row">1 blog post</div><div class="plan-row">up to 3,000 words</div><div class="plan-row">Unlimited Revised Posting</div></div>
  <a class="plan-btn" href="#">Choose Plan</a>
</div>

<!-- Testimonials -->
<h2 class="abs reviews-title h2">Hear from Our Happy Users</h2>
<div class="review faded" style="left:-170px"><p>Our clients love how easy it is to keep a steady stream of posts going every single week.</p></div>
<div class="review" style="left:145px"><div class="review-head"><div class="review-avatar" role="img" aria-label="Customer portrait"></div><div><div class="review-name">Nora L.</div><div class="stars">★★★★★<span>1 month ago</span></div></div></div><p>It is a long established fact that a reader will be distracted by the readable content of a page when looking at its layout. The point of using Lorem Ipsum is that it has a more-or-less normal distribution of letters, as opposed to using 'Content here, content here', making it look...</p></div>
<div class="review" style="left:475px"><div class="review-head"><div class="review-avatar" role="img" aria-label="Customer portrait"></div><div><div class="review-name">Lena &amp; Mark P.</div><div class="stars">★★★★★<span>1 month ago</span></div></div></div><p>It is a long established fact that a reader will be distracted by the readable content of a page when looking at its layout. The point of using Lorem Ipsum is that it has a more-or-less normal distribution of letters, as opposed to using 'Content here, content here', making it look...</p></div>
<div class="review" style="left:805px"><div class="review-head"><div class="review-avatar" role="img" aria-label="Customer portrait"></div><div><div class="review-name">Ivy K.</div><div class="stars">★★★★★<span>1 month ago</span></div></div></div><p>It is a long established fact that a reader will be distracted by the readable content of a page when looking at its layout. The point of using Lorem Ipsum is that it has a more-or-less normal distribution of letters, as opposed to using 'Content here, content here', making it look...</p></div>
<div class="review faded" style="left:1120px"><p>Our description is short and clear.</p></div>
<div class="abs dots"><i></i><i class="on"></i><i></i><i></i></div>

<!-- CTA -->
<svg class="abs cta-blob" viewBox="0 0 820 470" role="presentation"><defs><linearGradient id="blobFill" x1="0" y1="0" x2="1" y2="1"><stop offset="0" stop-color="#0094D4"/><stop offset="1" stop-color="#0054AA"/></linearGradient></defs><path d="M120 60 C260 -20 520 10 700 40 C800 60 820 140 820 200 L820 470 L60 470 C0 430 10 330 60 260 C110 190 40 110 120 60Z" fill="url(#blobFill)"/></svg>
<div class="abs cta-ring"></div>
<div class="abs cta-person" role="img" aria-label="Smiling woman working on a laptop"></div>
<div class="abs cta-content">
  <span class="badge badge-dark">Start Today</span>
  <h2>Transform Your Ideas into Reality – Sign Up for a Free Trial!</h2>
  <p>Everything you need to create and grow your blog: SEO tools, analytics, and more at your fingertips.</p>
  <a class="btn" href="#">Start Your 15 days Free Trial</a>
</div>

<!-- Footer -->
<footer class="abs footer">
  <div class="footer-row"><div class="brand"><span class="brand-dot"></span>PostNook</div><nav class="footer-links"><span>Home</span><span>Features</span><span>Pricing</span><span>How it Works</span><span>Blog</span><span>Resources</span><span>Contact Us</span></nav></div>
  <div class="footer-line"></div>
  <div class="footer-copy">© 2024 PostNook. All rights reserved.</div>
</footer>

</body>
</html>
```